7:35 Harbor Compass Method- A Handbook So Your Crew Trusts Each Step You Take

7:35 Harbor Compass Method
A Handbook So Your Crew Trusts Each Step You Take

It will be a 6 X 9 guide that is meant for people to keep with them with pages to fill out. See supporting pics for overall pillars that are discussed and form basis of the solution.

I will need a spine and back cover as well.

My blog and content: www.morvenqtallis.example

Target Market(s)

Business professionals, senior emergency services people

Industry/Entity Type

Business Management

Font styles to use
Serif

Colors

Designer to choose colors to be used in the design.

Requirements
Must have
• Clean look, easily recognizable among other books. Front cover and back and spine. My picture on the back somewhere (corner maybe?!)
Nice to have
• Easily recognizeable
• NOTE: Graphic should read Today, Did I Run My Crew As I Would Wish? I uploaded graphic that says ..."I Would've Wanted" which is incorrect.
Should not have
• Busy cover

```html
<!DOCTYPE html>
<html lang="en">
<head>
<meta charset="utf-8">
<title>Today, Did I Run My Crew As I Would Wish? — Cover Wrap</title>
<link rel="stylesheet" href="https://fonts.googleapis.com/css2?family=Sorts+Mill+Goudy&family=Ubuntu:wght@400&display=swap">
<style>
  :root {
    --paper: #ffffff;
    --blue-deep: #083a5e;
    --blue-mid: #0d6592;
    --blue-glow: #1d93bd;
    --title-white: #ffffff;
    --title-yellow: #c9cc12;
    --body-text: #ffffff;
    --spine-rule: #06324f;
    --photo-light: #7fdcf0;
    --photo-mid: #2aa9cf;
    --photo-dark: #0b4f78;
  }
  * { box-sizing: border-box; margin: 0; padding: 0; }
  html, body {
    width: 1200px; height: 1200px; overflow: hidden;
    background: var(--paper);
  }
  .canvas { position: relative; width: 1200px; height: 1200px; background: var(--paper); }

  .wrap {
    position: absolute; left: 0; top: 178px; width: 1200px; height: 844px;
    background:
      radial-gradient(ellipse 420px 420px at 330px 210px, rgba(40,160,205,.55), transparent 70%),
      radial-gradient(ellipse 460px 460px at 960px 320px, rgba(40,165,210,.6), transparent 70%),
      linear-gradient(180deg, var(--blue-mid) 0%, #0c5d88 45%, var(--blue-deep) 100%);
    overflow: hidden;
  }

  .serif { font-family: "Sorts Mill Goudy", "Goudy Old Style", Georgia, serif; font-weight: 400; }

  /* Back cover */
  .back-title {
    position: absolute; left: 80px; width: 200px; top: 78px;
    text-align: right; font-size: 33px; line-height: 34px;
    color: var(--title-white); letter-spacing: .5px;
  }
  .back-title .accent { color: var(--title-yellow); }
  .author-photo {
    position: absolute; left: 152px; top: 342px; width: 128px; height: 124px;
    background: radial-gradient(circle at 55% 40%, #b9a99a 0%, #6d5f55 45%, #2a2420 100%);
  }
  .back-copy {
    position: absolute; left: 306px; top: 148px; width: 200px;
    font-family: "Ubuntu", "Myriad Pro", Arial, sans-serif;
    font-size: 13.6px; line-height: 21.8px; color: var(--body-text);
    text-align: justify;
  }
  .back-copy p + p { margin-top: 21.8px; }

  /* Spine */
  .spine {
    position: absolute; left: 563px; top: 0; width: 75px; height: 844px;
    border-left: 1px solid var(--spine-rule);
    border-right: 1px solid var(--spine-rule);
  }
  .spine-text {
    position: absolute; top: 72px; white-space: nowrap;
    writing-mode: vertical-rl; font-size: 23px; letter-spacing: .3px;
  }
  .spine-title-1 { left: 36px; color: var(--title-white); }
  .spine-title-2 { left: 10px; color: var(--title-yellow); top: 198px; }
  .spine-author { left: 10px; top: 528px; color: var(--title-white); }

  /* Front cover */
  .front-title {
    position: absolute; left: 695px; top: 80px;
    font-size: 88px; line-height: 77.5px; letter-spacing: 2px;
    color: var(--title-white);
  }
  .front-title .accent { color: var(--title-yellow); }
  .front-author {
    position: absolute; left: 708px; top: 560px;
    font-size: 34px; letter-spacing: 1px; color: var(--title-white);
  }
  .front-photo {
    position: absolute; left: 638px; top: 628px; width: 562px; height: 216px;
    background:
      radial-gradient(ellipse 200px 160px at 300px 140px, rgba(11,60,95,.75), transparent 70%),
      linear-gradient(100deg, var(--photo-mid) 0%, var(--photo-light) 45%, var(--photo-mid) 75%, var(--photo-dark) 100%);
  }
</style>
</head>
<body>
<div class="canvas">
  <section class="wrap">
    <!-- Back cover -->
    <h2 class="back-title serif">TODAY,<br>DID I<br>RUN MY<br>CREW<br><span class="accent">AS I<br>WOULD<br>WISH?</span></h2>
    <div class="author-photo" role="img" aria-label="Portrait photo of the author"></div>
    <div class="back-copy">
      <p>Lorem ipsum dolor sit amet, consectetuer hutyu adipiscing elit. Aenean commodo ligula eget no dolor. Aenean massa. Cum sociis natoque nulla penatibus et magnis dissema parturient montes, nascetur ridiculus mus. Donec quamse felis, ultricies nec,pellentes que eu, pretium quis, sem. Nulla consequat massa quisat enim. Donec pede.</p>
      <p>In enim justo, rhoncus ut, are imperdiet a, venenatis vitae, justo. Nullam dictum felis eu pede mollis pretium. Integer tincidunt. Cras are dapibus. Vivamus elementum semper nisi. Aenean vulputate sempe eleifend tellus. Aenean leoade ligula, porttitor eu, consequat vitae, eleifend ac, enim. Aliquam lorem ante, dapibus in, viverra quis, feugiat a, tellus Egetnornullash vulputate sem Quisque semp rutrum enean.</p>
    </div>

    <!-- Spine -->
    <div class="spine">
      <span class="spine-text spine-title-1 serif">TODAY, DID I RUN MY CREW</span>
      <span class="spine-text spine-title-2 serif">AS I WOULD WISH?</span>
      <span class="spine-text spine-author serif">MORVEN Q TALLIS</span>
    </div>

    <!-- Front cover -->
    <h1 class="front-title serif">TODAY,<br>DID I RUN<br>MY CREW<br><span class="accent">AS I<br>WOULD<br>WISH?</span></h1>
    <p class="front-author serif">MORVEN Q TALLIS</p>
    <div class="front-photo" role="img" aria-label="Photo of a businessman in a suit with arms raised in celebration, tinted cyan"></div>
  </section>
</div>
</body>
</html>
```